'Cradle Ahead' promotional brochure

We have designed a 6 week program to educate impending first-time parents about the things they need to know to survive the first 6 months. Sessions delivered by general practitioner/family doctor, dietician, physiotherapist, speech pathologist and psychologist. Our promotional blurb is: 'A comprehensive education program for first-time parents-to-be, delivered over 6 weeks by health professionals in your community, about everything you need to know to look after your baby (and yourself!) in the first 6 months'. I now want to put together a promotional brochure to be distributed to those couples who express an interest which will provide further details of what will be delivered in the course.
Updates
In terms of layout, I envisaged a double sided A4 size, foldable into 3 sections, but very happy to be guided on this.
Target Market(s)
To appeal to a young, well educated demographic. First time parents couples.
Industry/Entity Type
Medical
Font styles to use
Other font styles liked:
- Playfair Display
Requirements
Must have
- Playfair display font to be consistent with our logo (attached). Logo also included please. Some consistency with colours of logo please.
Nice to have
- I am a doctor, and have no creative genes! But prefer a clean and professional appearance overall. Not too cluttered in overall appearance.
Should not have
- No cheesy pictures of babies.

```html
<!DOCTYPE html>
<html lang="en">
<head>
<meta charset="utf-8">
<title>Cradle Ahead brochure</title>
<link href="https://fonts.googleapis.com/css2?family=Playfair+Display:wght@400;700&display=swap" rel="stylesheet">
<style>
:root{
  --green:#3bb54a;
  --lime:#6cbf45;
  --pale-green:#8dd07a;
  --ink:#1e1e1e;
  --charcoal:#222;
  --grey:#8a8a8a;
  --paper:#f6f6f6;
  --row:#e6e6e6;
  --bg:#e9e9e9;
}
*{box-sizing:border-box;margin:0;padding:0}
html,body{width:869px;height:1200px;overflow:hidden}
body{background:var(--bg);font-family:"Playfair Display",Georgia,serif;color:var(--ink)}
.spread{position:absolute;left:56px;width:756px;height:534px;display:flex;overflow:hidden;box-shadow:0 3px 10px rgba(0,0,0,.25)}
.spread--inside{top:54px}
.spread--outside{top:612px}
.panel{position:relative;width:252px;height:100%;overflow:hidden}
.stripes{position:absolute;inset:0;pointer-events:none}
.panel--white{background:linear-gradient(90deg,#fff,#f1f1f1)}
.panel--grey{background:var(--grey)}
.panel--dark{background:var(--charcoal)}
.panel--lime{background:var(--lime)}
.panel--soft{background:linear-gradient(90deg,#f3f3f3,#e4e4e4)}
.panel--cover{background:linear-gradient(90deg,#f6f6f6,#ececec)}
.photo{position:absolute;left:0;right:0;bottom:0}
.card{position:absolute;left:30px;width:192px;border:1px solid var(--green);border-radius:96px 96px 0 0/12px 12px 0 0;padding:38px 14px 10px;font-size:7.4px;line-height:1.3;text-align:justify}
.card--black{border-color:var(--ink)}
.card--pale{border-color:var(--pale-green);color:#ddd}
.card--onGrey{border-color:var(--pale-green);color:#fff}
.badge{position:absolute;left:50%;top:-28px;transform:translateX(-50%);width:55px;height:55px;border-radius:50%;background:var(--green);color:#fff;display:flex;flex-direction:column;align-items:center;justify-content:center;font-weight:700;line-height:1}
.badge span{font-size:12px}
.badge b{font-size:17px;margin-top:2px}
.badge--black{background:var(--ink)}
.badge--pale{background:var(--pale-green)}
.card p+p{margin-top:8px}
.session{color:var(--green)}
.card--onGrey .session{color:#9be08a}
.card--black .session{color:var(--ink);font-weight:700}
.topics{list-style:none;margin:10px -14px 0}
.topics li{display:flex;align-items:center;gap:6px;padding:2.6px 14px;text-align:left}
.topics li:nth-child(odd){background:var(--row)}
.card--pale .topics li{padding:4px 14px}
.card--pale .topics li:nth-child(odd){background:#2c2c2c}
.tick{width:7px;height:7px;flex:none}
.contact{position:absolute;left:0;right:0;top:300px;text-align:center;font-size:7px;line-height:1.2}
.contact h2{color:var(--green);font-size:10px;font-weight:400;line-height:1.3;padding-bottom:4px;margin:0 auto 6px;width:150px;border-bottom:1px dashed var(--green)}
.contact p{margin-bottom:9px}
.contact p.tight{margin-bottom:1px}
.phone{position:absolute;left:0;right:0;top:464px;text-align:center;color:#fff;z-index:2}
.phone small{display:block;font-size:10px;font-weight:700}
.phone strong{font-size:22px;font-weight:700}
.brand{position:absolute;right:28px;top:22px;display:flex;align-items:center;gap:6px;color:var(--green);font-size:9px;line-height:1.05}
.brand i{width:14px;height:14px;background:var(--green);display:block}
.title{position:absolute;left:0;right:0;top:238px;text-align:center;color:var(--green);font-size:22px;font-weight:700}
.lede{position:absolute;left:8px;right:8px;top:274px;text-align:center;font-size:12.5px;font-weight:700;line-height:1.35;text-transform:uppercase}
.sub{position:absolute;left:8px;right:8px;top:332px;text-align:center;font-size:13px;line-height:1.25}
.small{position:absolute;left:8px;right:8px;top:378px;text-align:center;font-size:9.5px;line-height:1.3}
.cost{position:absolute;left:0;right:0;top:472px;text-align:center;color:#fff;font-size:13px;z-index:2}
.web{position:absolute;left:0;right:0;top:513px;text-align:center;color:#fff;font-size:6.5px;z-index:2}
.band{position:absolute;left:0;right:0;bottom:0}
</style>
</head>
<body>

<svg width="0" height="0" style="position:absolute">
  <defs>
    <symbol id="tick" viewBox="0 0 10 10"><path d="M1 5 L4 8 L9 2" fill="none" stroke="currentColor" stroke-width="2.4" stroke-linecap="round" stroke-linejoin="round"/></symbol>
  </defs>
</svg>

<!-- Inside spread -->
<section class="spread spread--inside">
  <div class="panel panel--white">
    <svg class="stripes" viewBox="0 0 252 534"><g stroke="var(--green)" stroke-width="9" stroke-linecap="round"><line x1="4" y1="8" x2="52" y2="50"/><line x1="-8" y1="28" x2="20" y2="52"/><line x1="258" y1="2" x2="212" y2="46"/></g></svg>
    <div class="card" style="top:66px">
      <div class="badge"><span>Week</span><b>1</b></div>
      <p>GP Dr Helen Marsh will share information for Mum's own health after delivery. Topics include:</p>
      <ul class="topics" style="color:var(--ink)">
        <li><svg class="tick" style="color:var(--green)"><use href="#tick"/></svg>Vaccinations in pregnancy</li>
        <li><svg class="tick" style="color:var(--green)"><use href="#tick"/></svg>Bleeding, bladder and bowel after delivery</li>
        <li><svg class="tick" style="color:var(--green)"><use href="#tick"/></svg>Breastfeeding, engorgement and mastitis</li>
        <li><svg class="tick" style="color:var(--green)"><use href="#tick"/></svg>Bottle feeding</li>
        <li><svg class="tick" style="color:var(--green)"><use href="#tick"/></svg>Post-natal anxiety &amp; depression</li>
        <li><svg class="tick" style="color:var(--green)"><use href="#tick"/></svg>Intimacy and contraception</li>
      </ul>
    </div>
    <div class="card" style="top:298px;height:208px">
      <div class="badge"><span>Week</span><b>2</b></div>
      <p><span class="session">Session 1</span> – Clinical Psychologist Dr Anna Reyes will discuss changes in relationships as couples become parents, gender roles in parenting and post-natal depression.</p>
      <p><span class="session">Session 2</span> – Physiotherapist Clare Holt will present advice for Mums regarding exercise during and after pregnancy, looking after the pelvic floor during and after pregnancy, and abdominal muscle separation management.</p>
      <p>She will also provide advice for promoting babies' neck strength and minimising the risk of flat spots on the head and encouraging gross motor skills in the first 6 months</p>
    </div>
  </div>

  <div class="panel panel--grey">
    <svg class="stripes" viewBox="0 0 252 534"><g stroke="var(--green)" stroke-width="9" stroke-linecap="round"><line x1="-6" y1="40" x2="32" y2="4"/><line x1="230" y1="4" x2="262" y2="34"/></g></svg>
    <div class="card card--onGrey" style="top:66px;height:252px">
      <div class="badge"><span>Week</span><b>3</b></div>
      <p><span class="session">Session 1</span> – Dietician Maya Singh provides advice for Mums regarding healthy eating during pregnancy and lactation, normal weight gain during pregnancy and realistic weight loss after. She will also discuss the evidence regarding breastfeeding VS bottle-feeding, normal infant weight gain and introducing solids (including those with potential for allergy).</p>
      <p><span class="session">Session 2</span> – Paediatric Speech Pathologist Ruth Ellis will share information about latching and breast-feeding troubles &amp; tongue tie, advice about dummies and finger-sucking, introducing solids &amp; feeding (including 'pouch' food), encouraging language development and current evidence about electronic devices impacting language development.</p>
    </div>
    <div class="photo" style="top:343px;background:linear-gradient(135deg,#d8d8d8,#9a9a9a 55%,#efefef)" role="img" aria-label="Black and white photo of a newborn's feet resting in a parent's hand"></div>
  </div>

  <div class="panel panel--dark">
    <svg class="stripes" viewBox="0 0 252 534"><g stroke-width="9" stroke-linecap="round"><line x1="-4" y1="2" x2="40" y2="44" stroke="var(--pale-green)"/><line x1="250" y1="4" x2="204" y2="50" stroke="var(--pale-green)"/><line x1="262" y1="24" x2="228" y2="58" stroke="var(--pale-green)"/></g></svg>
    <div class="card card--pale" style="top:70px;height:248px">
      <div class="badge badge--pale" style="color:var(--ink)"><span>Week</span><b>4</b></div>
      <p>GP Dr Helen Marsh will share advice about your babies' health in the first 6 months, including:</p>
      <ul class="topics">
        <li><svg class="tick" style="color:var(--pale-green)"><use href="#tick"/></svg>Skin of newborns</li>
        <li><svg class="tick" style="color:var(--pale-green)"><use href="#tick"/></svg>Sleeping</li>
        <li><svg class="tick" style="color:var(--pale-green)"><use href="#tick"/></svg>Crying</li>
        <li><svg class="tick" style="color:var(--pale-green)"><use href="#tick"/></svg>Immunisations</li>
        <li><svg class="tick" style="color:var(--pale-green)"><use href="#tick"/></svg>Fever and infections</li>
        <li><svg class="tick" style="color:var(--pale-green)"><use href="#tick"/></svg>Diarrhoea and constipation</li>
        <li><svg class="tick" style="color:var(--pale-green)"><use href="#tick"/></svg>Teething</li>
        <li><svg class="tick" style="color:var(--pale-green)"><use href="#tick"/></svg>Understanding a baby's signals</li>
      </ul>
    </div>
    <div class="photo" style="top:343px;background:linear-gradient(135deg,#cfcfcf,#8e8e8e 60%,#bdbdbd)" role="img" aria-label="Black and white photo of a baby's hand beside a stethoscope"></div>
  </div>
</section>

<!-- Outside spread -->
<section class="spread spread--outside">
  <div class="panel panel--lime">
    <svg class="stripes" viewBox="0 0 252 534"><g stroke="#9ad987" stroke-width="9" stroke-linecap="round"><line x1="4" y1="8" x2="52" y2="50"/><line x1="-8" y1="28" x2="20" y2="52"/><line x1="220" y1="44" x2="258" y2="6"/></g></svg>
    <div class="card card--black" style="top:72px;height:110px">
      <div class="badge badge--black"><span>Week</span><b>5</b></div>
      <p><span class="session">Session 1</span> – Clinical Psychologist Dr Anna Reyes will share information about bonding &amp; attachment with your baby, how to promote their social &amp; emotional development and how to manage separation anxiety. She will also discuss positive parenting approaches.</p>
    </div>
    <div class="card card--black" style="top:238px;height:147px">
      <div class="badge badge--black"><span>Week</span><b>6</b></div>
      <p><span class="session">Session 1</span> – Secret Men's Business – a men-only session (including beer!) with a new father for frank discussion about the road ahead. Mums will do a shopping excursion with the GP &amp; Dietician to Freshmart to look at baby products and food – the good and the bad!</p>
      <p><span class="session">Session 2</span> – Program review, reflection and evaluation and future session planning when baby is 6 months of age.</p>
    </div>
    <div class="photo" style="top:410px;background:linear-gradient(135deg,#a9dc8f,#5fae3c 55%,#9bd47f)" role="img" aria-label="Green-tinted photo of adult and baby hands holding a small heart"></div>
  </div>

  <div class="panel panel--soft">
    <svg class="stripes" viewBox="0 0 252 534"><g stroke="var(--green)" stroke-width="9" stroke-linecap="round"><line x1="-6" y1="40" x2="32" y2="4"/><line x1="180" y1="4" x2="262" y2="86"/><line x1="225" y1="0" x2="262" y2="38"/></g></svg>
    <div class="contact">
      <h2>CONTACT DETAILS<br>FOR ENQUIRIES/BOOKINGS</h2>
      <p class="tight">Wattlebrook Shopping Village, Shop 4</p>
      <p>12 Harbour Lane, Wattlebrook NSW 2999</p>
      <p>Fax: 02 5550 0199</p>
      <p>Email: reception@wattlebrookhealth.example</p>
      <p>Website: www.wattlebrookhealth.example</p>
    </div>
    <svg class="band" width="252" height="110" viewBox="0 0 252 110"><path d="M0 40 Q126 0 252 8 L252 110 L0 110Z" fill="var(--lime)"/><path d="M96 18 Q170 -2 252 8 L252 110 L110 110 Q90 60 96 18Z" fill="var(--green)"/></svg>
    <div class="phone"><small>Phone:</small><strong>(02) 5550 0188</strong></div>
  </div>

  <div class="panel panel--cover">
    <svg class="stripes" viewBox="0 0 252 534"><g stroke="var(--green)" stroke-width="9" stroke-linecap="round"><line x1="-10" y1="-10" x2="60" y2="60"/><line x1="240" y1="10" x2="210" y2="40"/><line x1="262" y1="22" x2="236" y2="48"/><line x1="262" y1="140" x2="224" y2="178"/></g><g stroke="#9ad987" stroke-width="9" stroke-linecap="round"><line x1="14" y1="4" x2="60" y2="48"/></g></svg>
    <div class="brand"><i></i><span>WATTLEBROOK<br>HEALTH &amp;<br>MEDICAL</span></div>
    <svg style="position:absolute;left:22px;top:56px" width="210" height="164" viewBox="0 0 210 164" role="img" aria-label="Heart-shaped photo of parents' hands holding a baby's hand">
      <defs><linearGradient id="heartFill" x1="0" y1="0" x2="1" y2="1"><stop offset="0" stop-color="var(--lime)"/><stop offset=".5" stop-color="#9a9a9a"/><stop offset="1" stop-color="var(--lime)"/></linearGradient></defs>
      <path d="M105 164 C60 120 0 90 0 46 C0 18 22 0 48 0 C74 0 95 16 105 34 C115 16 136 0 162 0 C188 0 210 18 210 46 C210 90 150 120 105 164Z" fill="url(#heartFill)"/>
    </svg>
    <div class="title">—CRADLE AHEAD—</div>
    <div class="lede">A comprehensive education program for first-time parents-to-be,</div>
    <div class="sub">delivered over 6 weeks by health professionals in your community,</div>
    <div class="small">about everything you need to know<br>to look after your baby (and yourself!)<br>in the <b>first 6 months</b></div>
    <svg class="band" width="252" height="106" viewBox="0 0 252 106"><path d="M0 10 Q126 -6 252 10 L252 106 L0 106Z" fill="var(--lime)"/><path d="M0 8 Q40 2 60 2 Q50 60 0 90Z" fill="var(--green)"/></svg>
    <div class="cost">Total Cost $300</div>
    <div class="web">www.wattlebrookhealth.example</div>
  </div>
</section>

</body>
</html>
```